Rolling Past Noon CD Cover

For this design, we would like you to use the attached picture as inspiration. The follow are the key things to consider: make the ground dirt instead of having a paved road, make the items the cart into things a hustling recording artist would be pushing like CD's, DVD's, tapes and also make it appear as if a few coins are falling from one of the bags, in the background turn the AC units into speakers, try to give the scene a musical vibe, the two men on the left side of the image should be black men with dreadlocks and the two on the right can remain as they are wearing turbans. We trust you'll incorporate some of your own creativity too. Use the same style for the for "The KOLV Circle" artist name along with the dividing line. The name of this record is called "Rolling Past Noon" Finally put the caption "ZEP 4.0" on one of the cart right above the wheel.

```html
<!DOCTYPE html>
<html lang="en">
<head>
<meta charset="utf-8">
<title>Rolling Past Noon — The KOLV Circle</title>
<link rel="stylesheet" href="https://fonts.googleapis.com/css2?family=Bebas+Neue&display=swap">
<style>
  :root {
    --backdrop-top: #4a4b33;
    --backdrop-bottom: #63653f;
    --sleeve: #1d1d20;
    --sleeve-edge: #2a2a2e;
    --accent-yellow: #e9e23a;
    --crowd-purple: #6a4a8c;
    --crowd-pink: #b86a9a;
    --crowd-green: #6f8d4e;
    --crowd-sand: #c9b59a;
    --crowd-shadow: #3a2f40;
  }
  html, body {
    margin: 0;
    padding: 0;
    width: 1200px;
    height: 866px;
    overflow: hidden;
  }
  body {
    background: linear-gradient(180deg, var(--backdrop-top), var(--backdrop-bottom));
    position: relative;
  }
  .album-cover {
    position: absolute;
    left: 255px;
    top: 85px;
    width: 689px;
    height: 696px;
    background: linear-gradient(160deg, var(--sleeve-edge), var(--sleeve) 45%);
    box-shadow: 0 18px 40px rgba(0,0,0,0.35);
  }
  .album-cover svg {
    display: block;
    width: 100%;
    height: 100%;
  }
  .artist-name,
  .album-title,
  .edition-label {
    font-family: "Bebas Neue", "Oswald", sans-serif;
  }
  .artist-name { fill: var(--accent-yellow); font-size: 64px; }
  .album-title {
    font-size: 160px;
    fill: url(#crowd-tones);
    stroke: var(--accent-yellow);
    stroke-width: 1.6px;
  }
  .edition-label { fill: var(--accent-yellow); font-size: 18px; letter-spacing: 0.5px; }
  .photo-strip-frame { fill: none; stroke: var(--accent-yellow); stroke-width: 1.6px; }
</style>
</head>
<body>
  <div class="album-cover">
    <svg viewBox="0 0 530 535" xmlns="http://www.w3.org/2000/svg">
      <defs>
        <linearGradient id="crowd-tones" x1="0" y1="0" x2="1" y2="1">
          <stop offset="0" stop-color="var(--crowd-sand)"/>
          <stop offset="0.25" stop-color="var(--crowd-purple)"/>
          <stop offset="0.45" stop-color="var(--crowd-shadow)"/>
          <stop offset="0.65" stop-color="var(--crowd-pink)"/>
          <stop offset="0.85" stop-color="var(--crowd-green)"/>
          <stop offset="1" stop-color="var(--crowd-purple)"/>
        </linearGradient>
        <linearGradient id="strip-tones" x1="0" y1="0" x2="0.4" y2="1">
          <stop offset="0" stop-color="var(--crowd-sand)"/>
          <stop offset="0.3" stop-color="var(--crowd-purple)"/>
          <stop offset="0.55" stop-color="var(--crowd-pink)"/>
          <stop offset="0.8" stop-color="var(--crowd-shadow)"/>
          <stop offset="1" stop-color="var(--crowd-purple)"/>
        </linearGradient>
      </defs>

      <text class="artist-name" x="38" y="95" textLength="379" lengthAdjust="spacingAndGlyphs">THE KOLV CIRCLE</text>

      <g role="img" aria-label="Album title lettering filled with a photo of a crowd dancing under clouds of coloured powder">
        <text class="album-title" x="38" y="215" textLength="380" lengthAdjust="spacingAndGlyphs">ROLLING</text>
        <text class="album-title" x="38" y="331" textLength="228" lengthAdjust="spacingAndGlyphs">PAST</text>
        <text class="album-title" x="38" y="447" textLength="250" lengthAdjust="spacingAndGlyphs">NOON</text>
      </g>

      <text class="edition-label" x="300" y="447">ZEP 4.0</text>

      <rect class="photo-strip" x="433" y="103" width="89" height="344" fill="url(#strip-tones)"
            role="img" aria-label="Photo of festival-goers covered in coloured powder, dancing and laughing"/>
      <rect class="photo-strip-frame" x="433" y="103" width="89" height="344"/>
    </svg>
  </div>
</body>
</html>
```